Land Buying Company Needs Letterhead for Direct Mail Marketing to Land Owners

We are looking for a professional letterhead that we will be including in our direct mail marketing. We will be sending this to land owners who may be interested in selling or purchasing land.

The letterhead needs to be editable. Headers and footers would look nice, but we are open. We would want it to include our address, website, phone, and email info. For right now the address to use for design purposes would the following:

Address: 415 Bramwell Avenue #600
Dallas, TX 75219
Website - www.quillridgeacres.example
Email - info@quillridgeacres.example
Phone - 866-402-ACRE

I have attached our logo zip file that we just had done on Pixel Guild. Let me know what questions you have, and thank you.

```html
<!DOCTYPE html>
<html lang="en">
<head>
<meta charset="utf-8">
<title>Quill Ridge Acres Letterhead</title>
<link href="https://fonts.googleapis.com/css2?family=Montserrat:wght@400;500;600;700&display=swap" rel="stylesheet">
<style>
  :root {
    --forest: #455f2c;
    --leaf: #8cc63f;
    --ink: #1f1f1f;
    --paper: #ffffff;
    --stage: #f0f0f0;
    --mist: #f1f1ef;
  }
  * { box-sizing: border-box; margin: 0; padding: 0; }
  html, body { width: 1200px; height: 943px; overflow: hidden; }
  body {
    background: var(--stage);
    font-family: "Montserrat", sans-serif;
    color: var(--ink);
    position: relative;
  }
  .sheet {
    position: absolute;
    top: 130px;
    width: 480px;
    height: 679px;
    background: var(--paper);
    box-shadow: 0 0 18px rgba(0,0,0,0.12);
    overflow: hidden;
  }
  .sheet--blank { left: 90px; }
  .sheet--letter { left: 624px; }

  .brand {
    position: absolute;
    top: 29px;
    left: 0;
    width: 100%;
    display: flex;
    align-items: center;
    justify-content: center;
    gap: 12px;
  }
  .brand__dot {
    width: 54px;
    height: 54px;
    border-radius: 50%;
    background: var(--forest);
  }
  .brand__name {
    font-weight: 700;
    font-size: 20px;
    letter-spacing: 1.5px;
    text-transform: uppercase;
    color: var(--forest);
    white-space: nowrap;
  }

  .backdrop {
    position: absolute;
    left: 111px;
    top: 212px;
    width: 258px;
    height: 258px;
    border-radius: 50%;
    background: var(--mist);
  }
  .sheet--letter .backdrop { opacity: 0.75; }

  .letter {
    position: absolute;
    left: 51px;
    top: 146px;
    width: 378px;
    font-size: 9.3px;
    letter-spacing: -0.1px;
    line-height: 11.3px;
  }
  .letter__recipient { margin-bottom: 29px; font-size: 9.8px; letter-spacing: 0; }
  .letter__subject {
    font-weight: 600;
    font-size: 11px;
    letter-spacing: 0;
    margin-bottom: 29px;
    white-space: nowrap;
  }
  .letter__body p {
    text-align: justify;
    margin-bottom: 11.3px;
  }
  .letter__body p.indent { text-indent: 28px; }
  .letter__closing { margin-top: 34px; font-size: 9.8px; letter-spacing: 0; }
  .letter__signature {
    margin-top: 16px;
    width: 122px;
    height: 32px;
    background: linear-gradient(90deg, rgba(40,40,40,0.16), rgba(40,40,40,0.06));
    border-radius: 4px;
  }

  .contact {
    position: absolute;
    top: 611px;
    left: 69px;
    display: flex;
    font-size: 9.8px;
    line-height: 11.3px;
    white-space: nowrap;
  }
  .contact__label { color: var(--forest); font-weight: 500; }
  .contact__divider {
    width: 2px;
    height: 30px;
    margin: 2px 17px 0 0;
    background: var(--forest);
  }
  .contact__block--address { width: 139px; }

  .site-band {
    position: absolute;
    left: 0;
    bottom: 0;
    width: 100%;
    height: 29px;
    background: var(--forest);
    color: #fff;
    font-weight: 500;
    font-size: 11px;
    letter-spacing: 0.3px;
    display: flex;
    align-items: center;
    justify-content: center;
  }
</style>
</head>
<body>

  <section class="sheet sheet--blank">
    <header class="brand">
      <span class="brand__dot"></span>
      <span class="brand__name">Quill Ridge Acres</span>
    </header>
    <div class="backdrop" role="img" aria-label="Faint decorative emblem area"></div>
    <footer>
      <div class="contact">
        <div class="contact__block contact__block--address">
          <div class="contact__label">Address:</div>
          <div>415 Bramwell Avenue #600</div>
          <div>Dallas, TX 75219</div>
        </div>
        <span class="contact__divider"></span>
        <div class="contact__block">
          <div class="contact__label">Contact:</div>
          <div>Phone - 866-402-ACRE</div>
          <div>Email - info@quillridgeacres.example</div>
        </div>
      </div>
      <div class="site-band">www.quillridgeacres.example</div>
    </footer>
  </section>

  <section class="sheet sheet--letter">
    <header class="brand">
      <span class="brand__dot"></span>
      <span class="brand__name">Quill Ridge Acres</span>
    </header>
    <div class="backdrop" role="img" aria-label="Faint decorative emblem area"></div>
    <article class="letter">
      <div class="letter__recipient">
        To,<br>Director<br>Quill Ridge Acres<br>Texas
      </div>
      <div class="letter__subject">Sub: Lorem ipsum dolor sit amet, consectetur adipiscing elit.</div>
      <div class="letter__body">
        <p class="indent">Lorem ipsum dolor sit amet, consectetur adipiscing elit, sed do eiusmod tempor incididunt ut labore et dolore magna aliqua. Quis ipsum suspendisse ultrices gravida. Risus commodo viverra maecenas accumsan lacus vel facilisis.</p>
        <p>Lorem ipsum dolor sit amet, consectetur adipiscing elit, sed do eiusmod tempor incididunt ut labore et dolore magna aliqua. Quis ipsum suspendisse ultrices gravida. Risus commodo viverra maecenas accumsan lacus vel facilisis. Lorem ipsum dolor sit amet, consectetur adipiscing elit, sed do eiusmod tempor incididunt ut labore et dolore magna aliqua. Quis ipsum suspendisse ultrices gravida. Risus commodo viverra maecenas accumsan lacus vel facilisis. Lorem ipsum dolor sit amet, consectetur adipiscing elit, sed do eiusmod tempor incididunt ut labore et dolore magna aliqua. Quis ipsum suspendisse ultrices gravida. Risus commodo viverra maecenas accumsan lacus vel facilisis.</p>
        <p>Lorem ipsum dolor sit amet, consectetur adipiscing elit, sed do eiusmod tempor incididunt ut labore et dolore magna aliqua.</p>
      </div>
      <div class="letter__closing">With Regards</div>
      <div class="letter__signature" role="img" aria-label="Handwritten signature"></div>
    </article>
    <footer>
      <div class="contact">
        <div class="contact__block contact__block--address">
          <div class="contact__label">Address:</div>
          <div>415 Bramwell Avenue #600</div>
          <div>Dallas, TX 75219</div>
        </div>
        <span class="contact__divider"></span>
        <div class="contact__block">
          <div class="contact__label">Contact:</div>
          <div>Phone - 866-402-ACRE</div>
          <div>Email - info@quillridgeacres.example</div>
        </div>
      </div>
      <div class="site-band">www.quillridgeacres.example</div>
    </footer>
  </section>

</body>
</html>
```